New Webpage for High Class Expert Witness Services Company

We are looking for a minimalist design for a webpage that just has our logo and an entry form offer to connect with one of our Liaisons.
The entry form should just ask for Name, Email, Contact Info and Description of Project.

Company Name is: The Marlowe Crest Defense Services

Number of Pages Required

1 page

```html
<!DOCTYPE html>
<html lang="en">
<head>
<meta charset="UTF-8">
<title>The Marlowe Crest Defense Services — Connect With A Liaison</title>
<link href="https://fonts.googleapis.com/css2?family=Cinzel:wght@500;600&family=Poppins:wght@400;500;600&display=swap" rel="stylesheet">
<style>
  :root {
    --bg: #050505;
    --card: #070707;
    --card-border: #2a2a2a;
    --field: #0e0e0f;
    --field-border: #2c2c2e;
    --text: #f2f2f2;
    --muted: #8a8a8d;
    --silver-1: #b9babd;
    --silver-2: #e2e3e5;
    --line: #3a3a3a;
  }
  * { box-sizing: border-box; margin: 0; padding: 0; }
  html, body { width: 1079px; height: 1200px; overflow: hidden; background: var(--bg); }
  body { position: relative; font-family: 'Poppins', sans-serif; color: var(--text); }

  .backdrop {
    position: absolute; inset: 0;
    background:
      radial-gradient(ellipse 900px 300px at 50% 105%, rgba(255,255,255,0.07), transparent 70%),
      radial-gradient(ellipse 700px 220px at 80% 70%, rgba(255,255,255,0.06), transparent 70%),
      radial-gradient(ellipse 600px 260px at 5% 60%, rgba(255,255,255,0.05), transparent 70%),
      linear-gradient(180deg, #0b0b0b 0%, #030303 45%, #0a0a0a 100%);
  }

  .brand {
    position: absolute; top: 66px; left: 0; width: 100%;
    display: flex; justify-content: center; align-items: center; gap: 12px;
  }
  .brand-mark { width: 14px; height: 14px; background: var(--silver-2); }
  .brand-name {
    font-family: 'Cinzel', serif; font-weight: 600; font-size: 25px;
    color: var(--silver-2); letter-spacing: 0.5px;
  }

  .divider {
    position: absolute; left: 50%; transform: translateX(-50%);
    display: flex; align-items: center; gap: 10px;
  }
  .divider span { height: 1px; background: var(--line); }
  .divider i { width: 11px; height: 11px; background: var(--silver-2); display: block; }

  .liaison-card {
    position: absolute; left: 267px; top: 154px; width: 545px; height: 608px;
    background: var(--card); border: 1px solid var(--card-border); border-radius: 19px;
  }
  .liaison-title {
    position: absolute; top: 190px; left: 0; width: 100%; text-align: center;
    font-family: 'Cinzel', serif; font-weight: 600; font-size: 28px; letter-spacing: 0.5px;
  }
  .liaison-intro {
    position: absolute; top: 226px; left: 0; width: 100%; text-align: center;
    font-size: 11.5px; line-height: 18px;
  }

  .field-label { position: absolute; left: 320px; font-size: 10.8px; }
  .field {
    position: absolute; left: 320px; width: 438px;
    background: var(--field); border: 1px solid var(--field-border); border-radius: 5px;
    display: flex; align-items: center; gap: 10px; padding: 0 12px;
    font-size: 10.2px; color: var(--muted);
  }
  .field svg { width: 13px; height: 13px; stroke: var(--muted); fill: none; stroke-width: 1.3; flex: none; }
  .field--area { align-items: flex-start; padding-top: 15px; }

  .submit {
    position: absolute; left: 320px; top: 682px; width: 438px; height: 48px;
    border-radius: 5px; background: linear-gradient(90deg, var(--silver-1), var(--silver-2));
    color: #111; font-weight: 600; font-size: 11px; letter-spacing: 0.2px;
    display: flex; align-items: center; justify-content: center;
  }

  .touch-title {
    position: absolute; top: 830px; left: 0; width: 100%; text-align: center;
    font-family: 'Cinzel', serif; font-weight: 600; font-size: 27px; letter-spacing: 0.5px;
  }

  .info-card {
    position: absolute; top: 958px; width: 253px; height: 136px;
    background: var(--card); border: 1px solid #1f1f1f; border-radius: 10px; text-align: center;
  }
  .info-icon {
    position: absolute; top: -25px; left: 98px; width: 57px; height: 57px; border-radius: 10px;
    background: linear-gradient(135deg, #eeeeef, #bcbdc0);
    display: flex; align-items: center; justify-content: center;
  }
  .info-icon svg { width: 28px; height: 28px; }
  .info-title { margin-top: 51px; font-size: 16.5px; font-weight: 500; }
  .info-text { margin-top: 6px; font-size: 11.5px; line-height: 18.5px; white-space: nowrap; }

  .footer-rule { position: absolute; top: 1146px; left: 127px; width: 824px; height: 1px; background: #222; }
  .footer-note { position: absolute; top: 1165px; left: 0; width: 100%; text-align: center; font-size: 11.5px; }
</style>
</head>
<body>
  <div class="backdrop" role="img" aria-label="Dark flowing satin waves in black and charcoal"></div>

  <header class="brand">
    <div class="brand-mark"></div>
    <div class="brand-name">MARLOWE CREST DEFENSE SERVICES</div>
  </header>

  <section class="liaison-card"></section>
  <h1 class="liaison-title">CONNECT WITH A LIAISON</h1>
  <p class="liaison-intro">High-Class Expert Witness Support. Share Your Project Details And A<br>Dedicated Liaison Will Reach You Within 24 Hours.</p>
  <div class="divider" style="top:281px"><span style="width:122px"></span><i></i><span style="width:122px"></span></div>

  <label class="field-label" style="top:316px">Full Name *</label>
  <div class="field" style="top:340px;height:41px">
    <svg viewBox="0 0 16 16"><circle cx="8" cy="5" r="3"/><path d="M2.5 15c0-3 2.5-5 5.5-5s5.5 2 5.5 5"/></svg>First Name
  </div>

  <label class="field-label" style="top:392px">Email Address *</label>
  <div class="field" style="top:415px;height:41px">
    <svg viewBox="0 0 16 16"><path d="M1.5 6.5 8 2l6.5 4.5V14h-13z"/><path d="M1.5 6.5 8 10.5l6.5-4"/></svg>Your Email
  </div>

  <label class="field-label" style="top:467px;left:322px">Contact Info (Phone / Direct Line) *</label>
  <div class="field" style="top:491px;height:41px">
    <svg viewBox="0 0 16 16"><path d="M3 1.8 5.3 1.5 6.5 4.5 5 5.8c.8 1.8 2.3 3.3 4.2 4.2l1.3-1.5 3 1.2-.3 2.3c-.2.9-1 1.5-1.9 1.5C6.6 13.5 2.5 9.4 2.5 4.7c0-.9.6-1.7 1.5-1.9z"/><path d="M10 2v3M12.5 2v3"/></svg>Phone
  </div>

  <label class="field-label" style="top:544px">Description Of Project *</label>
  <div class="field field--area" style="top:567px;height:98px">
    <svg viewBox="0 0 16 16"><path d="M8 2C4.4 2 1.5 4.4 1.5 7.3c0 1.5.8 2.9 2 3.8L3 14l3.3-1.7c.5.1 1.1.2 1.7.2 3.6 0 6.5-2.4 6.5-5.2S11.6 2 8 2z"/><path d="M5 6.5h6M5 8.5h4"/></svg>Provide Key Case Details, Litigation Area, Required Expertise, Deadlines...
  </div>

  <div class="submit">SUBMIT NOW</div>

  <h2 class="touch-title">GET IN TOUCH</h2>
  <div class="divider" style="top:877px"><span style="width:70px"></span><i></i><span style="width:70px"></span></div>

  <article class="info-card" style="left:127px">
    <div class="info-icon"><svg viewBox="0 0 24 24"><path fill="#111" d="M12 1.5c-4.1 0-7.2 3.1-7.2 7.1 0 4.9 7.2 13.9 7.2 13.9s7.2-9 7.2-13.9c0-4-3.1-7.1-7.2-7.1zm0 9.6a2.6 2.6 0 1 1 0-5.2 2.6 2.6 0 0 1 0 5.2z"/></svg></div>
    <h3 class="info-title">Contact Details</h3>
    <p class="info-text">Suite 4100, Building 3, Floor 22, 48210<br>North Harbor Park West, Suite 512C</p>
  </article>

  <article class="info-card" style="left:413px">
    <div class="info-icon"><svg viewBox="0 0 24 24"><rect x="1.5" y="4" width="21" height="16" rx="2" fill="#111"/><path d="M3.5 6.5 12 13l8.5-6.5M3.5 18l6.5-5.5M20.5 18 14 12.5" stroke="#e6e6e7" stroke-width="1.4" fill="none"/></svg></div>
    <h3 class="info-title">Email Address</h3>
    <p class="info-text">Info@Marlowecrest.Com</p>
  </article>

  <article class="info-card" style="left:698px">
    <div class="info-icon"><svg viewBox="0 0 24 24"><path fill="#111" d="M6.6 3.2 9 2.8l1.6 4.3-2 1.6c1 2.3 2.8 4.2 5.1 5.3l1.7-1.9 4.2 1.7-.4 2.5c-.2 1.2-1.3 2.1-2.6 2-7.1-.5-12.8-6.2-13.3-13.3-.1-1.3.8-2.5 2.1-2.7z"/><path d="M14 3.5a6.5 6.5 0 0 1 6.5 6.5M14 6.5a3.5 3.5 0 0 1 3.5 3.5" stroke="#111" stroke-width="1.6" fill="none"/></svg></div>
    <h3 class="info-title">Phone Number</h3>
    <p class="info-text">-61 (555) 014 2290</p>
  </article>

  <div class="footer-rule"></div>
  <footer class="footer-note">2026 The Marlowe Crest Defense Services All Right</footer>
</body>
</html>
```